Stonebrook Glazeworks Inc. Business Card

Looking for business card with embossed raised logo print. Logo provided and want it to be most prominent image on card. Color pallet of black, red, white or charcoal gray preferred for brand recognition. Simple contact information on front and list description of services provided on back. Services included....Custom Showers, Tub Surrounds, Backsplashes, Fireplaces, Floors and more. Dustless Demolition, Lifetime Warranty, Proud member of the Federated Surface Installers Guild

Target Market(s)

High end residential remodel work and new home builders

Contact Information for Business Card

Phone # (402) 555-0193 email address, Stonebrookgw@mailvane.net Dorian Kovalski Owner

Requirements
Must have
• Business logo as most prominent image on the front of business card. Along with contact information and name Dorian Kovalski. Would like to see services provided on the back of the card.

```html
<!DOCTYPE html>
<html lang="en">
<head>
<meta charset="utf-8">
<title>Stonebrook Glazeworks Inc. Business Card</title>
<link href="https://fonts.googleapis.com/css2?family=Lato:wght@400;700&display=swap" rel="stylesheet">
<style>
  :root {
    --stage: #5f5f5f;
    --red: #e01e24;
    --black: #0a0a0a;
    --ink: #1b1b1b;
    --white: #ffffff;
    --tile-dark: #140c0b;
    --tile-brown: #3a2320;
  }
  * { box-sizing: border-box; margin: 0; padding: 0; }
  html, body { width: 1200px; height: 1200px; overflow: hidden; }
  body {
    background: var(--stage);
    font-family: 'Lato', sans-serif;
    position: relative;
  }
  .card {
    position: absolute;
    left: 240px;
    width: 720px;
    height: 420px;
    border-radius: 14px;
    overflow: hidden;
  }
  .card-front { top: 142px; background: var(--black); }
  .card-back { top: 638px; background: var(--white); }

  .tile-pattern {
    position: absolute;
    inset: 0;
    background: linear-gradient(135deg, var(--tile-brown) 0%, var(--tile-dark) 55%, var(--black) 100%);
  }
  .brand {
    position: absolute;
    display: flex;
    align-items: center;
    gap: 14px;
  }
  .brand-square { background: var(--red); flex: none; }
  .brand-name {
    color: var(--red);
    font-family: 'Lato', sans-serif;
    font-weight: 700;
    text-transform: uppercase;
    line-height: 1.05;
  }
  .card-front .brand { right: 26px; bottom: 40px; }
  .card-front .brand-square { width: 64px; height: 64px; }
  .card-front .brand-name { font-size: 32px; letter-spacing: 1px; }

  .card-back .brand { left: 24px; top: 68px; }
  .card-back .brand-square { width: 54px; height: 54px; }
  .card-back .brand-name { font-size: 26px; letter-spacing: 0.5px; }

  .contact { position: absolute; left: 24px; top: 168px; color: var(--ink); }
  .contact-name { color: var(--red); font-weight: 700; font-size: 27px; line-height: 34px; }
  .contact-title { font-size: 21px; line-height: 30px; }
  .contact-line { display: flex; align-items: center; gap: 9px; font-size: 21px; line-height: 35px; }
  .contact-line svg { width: 20px; height: 20px; fill: var(--red); flex: none; }

  .divider {
    position: absolute;
    left: 407px;
    top: 70px;
    width: 2px;
    height: 225px;
    background: var(--red);
  }
  .services {
    position: absolute;
    left: 454px;
    top: 60px;
    list-style: none;
  }
  .services li {
    display: flex;
    align-items: center;
    gap: 10px;
    font-size: 22px;
    line-height: 35px;
    color: var(--ink);
  }
  .services li::before {
    content: "";
    width: 16px;
    height: 16px;
    border-radius: 50%;
    background: var(--red);
    flex: none;
  }
  .membership {
    position: absolute;
    left: 0; right: 0; bottom: 0;
    height: 66px;
    background: var(--black);
    color: var(--red);
    font-weight: 700;
    font-size: 22px;
    display: flex;
    align-items: center;
    justify-content: center;
  }
</style>
</head>
<body>
  <section class="card card-front">
    <div class="tile-pattern" role="img" aria-label="Repeating dark brown tile pattern"></div>
    <div class="brand">
      <span class="brand-square"></span>
      <span class="brand-name">Stonebrook<br>Glazeworks Inc.</span>
    </div>
  </section>

  <section class="card card-back">
    <div class="brand">
      <span class="brand-square"></span>
      <span class="brand-name">Stonebrook<br>Glazeworks Inc.</span>
    </div>
    <div class="contact">
      <p class="contact-name">Dorian Kovalski</p>
      <p class="contact-title">General Manager</p>
      <p class="contact-line">
        <svg viewBox="0 0 24 24" aria-hidden="true"><path d="M3 9c0-3 4-5 9-5s9 2 9 5v2h-5V9c-1-.7-2.5-1-4-1s-3 .3-4 1v2H3z"/><path d="M6 12h12l2 8H4z M12 14a2.5 2.5 0 1 0 0 5a2.5 2.5 0 1 0 0-5z"/></svg>
        <span>(402) 555-0193</span>
      </p>
      <p class="contact-line">
        <svg viewBox="0 0 24 24" aria-hidden="true"><path d="M2 5h20v14H2z M4 7l8 6 8-6v-.2H4z" fill-rule="evenodd"/></svg>
        <span>Stonebrookgw@mailvane.net</span>
      </p>
    </div>
    <div class="divider"></div>
    <ul class="services">
      <li>Custom Showers</li>
      <li>Tub Surrounds</li>
      <li>Backsplashes</li>
      <li>Fireplaces</li>
      <li>Floors and more</li>
      <li>Dustless Demolition</li>
      <li>Lifetime Warranty</li>
    </ul>
    <p class="membership">Proud member of the Federated Surface Installers Guild</p>
  </section>
</body>
</html>
```